Business cards for law firm with global theme

I'd like business cards with contact info for two offices. They should include the colors and font of the new logo design, which is a stylized globe with an "F" in it. The feel should be very modern and professional.

```html
<!DOCTYPE html>
<html lang="en">
<head>
<meta charset="utf-8">
<title>Valmonte Law – Business Cards</title>
<link href="https://fonts.googleapis.com/css2?family=Source+Sans+3:wght@400;600;700&display=swap" rel="stylesheet">
<style>
  :root {
    --backdrop: #e6e6e6;
    --navy: #133c6d;
    --navy-deep: #0c2a52;
    --pattern-light: #5f82bb;
    --sky: #2a9fd8;
    --paper: #f4f4f4;
    --white: #ffffff;
  }
  * { margin: 0; padding: 0; box-sizing: border-box; }
  html, body {
    width: 1200px; height: 960px; overflow: hidden;
    background: var(--backdrop);
    font-family: "Source Sans 3", "Source Sans Pro", Arial, sans-serif;
  }
  .canvas { position: relative; width: 1200px; height: 960px; }

  .card { position: absolute; left: 297px; width: 610px; height: 349px; overflow: hidden; }

  /* Front */
  .card-front { top: 102px; background: var(--navy); }
  .front-pattern {
    position: absolute; inset: 0;
    background: linear-gradient(90deg, var(--pattern-light) 0%, #34589a 35%, var(--navy) 65%, var(--navy-deep) 100%);
    opacity: 0.75;
  }
  .front-brand {
    position: absolute; left: 312px; top: 212px;
    display: flex; align-items: center; gap: 12px;
  }
  .brand-dot { width: 60px; height: 60px; border-radius: 50%; background: var(--sky); flex: none; }
  .brand-name {
    font-weight: 700; font-size: 27px; letter-spacing: 0.5px; color: var(--white); white-space: nowrap;
  }

  /* Back */
  .card-back { top: 505px; background: var(--paper); }
  .back-brand {
    position: absolute; left: 40px; top: 100px; width: 240px;
    display: flex; flex-direction: column; align-items: center; gap: 14px;
  }
  .back-brand .brand-dot { width: 76px; height: 76px; background: var(--navy); }
  .back-brand .brand-name { color: var(--navy); font-size: 31px; }

  .divider { position: absolute; left: 303px; top: 99px; width: 3px; height: 140px; background: var(--sky); }

  .contact { position: absolute; left: 341px; top: 106px; color: var(--navy); }
  .person-name { font-size: 20px; font-weight: 700; color: var(--sky); line-height: 24px; }
  .person-title { font-size: 15.5px; line-height: 22px; margin-bottom: 16px; }
  .contact-list { list-style: none; }
  .contact-list li {
    display: flex; align-items: center; gap: 6px;
    font-size: 15.5px; line-height: 20.5px;
  }
  .contact-list svg { width: 14px; height: 14px; flex: none; }

  .offices {
    position: absolute; left: 0; right: 0; top: 283px;
    text-align: center; color: var(--navy); font-size: 15.5px; line-height: 20px;
  }
</style>
</head>
<body>
<main class="canvas">

  <section class="card card-front" aria-label="Card front">
    <div class="front-pattern" role="img" aria-label="Repeating grid of globe marks fading from light to dark blue"></div>
    <div class="front-brand">
      <span class="brand-dot"></span>
      <span class="brand-name">VALMONTE LAW</span>
    </div>
  </section>

  <section class="card card-back" aria-label="Card back">
    <div class="back-brand">
      <span class="brand-dot"></span>
      <span class="brand-name">VALMONTE LAW</span>
    </div>

    <div class="divider"></div>

    <div class="contact">
      <p class="person-name">Daniel Harper</p>
      <p class="person-title">Attorney at Law</p>
      <ul class="contact-list">
        <li>
          <svg viewBox="0 0 16 16" fill="none" stroke="#133c6d" stroke-width="1.5"><path d="M3 1.5h3l1.2 3.2-1.8 1.2a8 8 0 0 0 4.7 4.7l1.2-1.8 3.2 1.2v3a1.5 1.5 0 0 1-1.5 1.5A12.5 12.5 0 0 1 1.5 3 1.5 1.5 0 0 1 3 1.5z"/></svg>
          (555) 014-2290
        </li>
        <li>
          <svg viewBox="0 0 16 16" fill="none" stroke="#133c6d" stroke-width="1.5"><rect x="1.5" y="3" width="13" height="10"/><path d="M1.5 3.5 8 9l6.5-5.5"/></svg>
          daniel@valmontelaw.com
        </li>
        <li>
          <svg viewBox="0 0 16 16" fill="none" stroke="#133c6d" stroke-width="1.3"><circle cx="8" cy="8" r="6.5"/><ellipse cx="8" cy="8" rx="2.8" ry="6.5"/><path d="M1.5 8h13"/></svg>
          www.valmontelaw.com
        </li>
      </ul>
    </div>

    <address class="offices" style="font-style:normal">
      88 Mercer Ave. Ste. 210, NYC, NY 10013<br>
      340 Mercer Ave. Ste. 512, NYC, NY 10013
    </address>
  </section>

</main>
</body>
</html>
```